Folderdesign für Hundeshop und Hundesalon Pfote Mirella
Zielgruppe
Hundesalon ( pfote-mirella.de)
Hundeshop mit Onlineshop (hundeshop-pfote-mirella.de)
Zielgruppe: Hundebesitzer
Aufgabenstellung
Das Design sollte klar strukturiert und keinesfalls überladen sein, sondern mit einem Blick gut zu erfassen sein, farblich passend zu Naturkauartikeln, Kauartikeln ohne chem. Zusatzstoffe,...s Homepage
Erste Seite soll Hundesalon UND Hundeshop bewerben
Hervorgehoben werden soll der Hundeshop, da er als Onlineshop neu ist. Die Informationen entnehmen Sie bitte der HP www.hundeshop-pfote-mirella.de.
Der Hundesalon soll eine Seite bekommen
DIN A 4 Wickelfalz, 6seitig...lasse mich aber gerne beraten falls jemand etwas anderes besser findet
Habe schon mal einen Flyer entworfen, aber er sieht mir zu normal und einfach aus. Texte können auch gerne verändert werden

```html
<!DOCTYPE html>
<html lang="de">
<head>
<meta charset="utf-8">
<title>Folder Pfote Mirella – Hundesalon + Shop</title>
<link href="https://fonts.googleapis.com/css2?family=Great+Vibes&family=Open+Sans:wght@400;600;700&display=swap" rel="stylesheet">
<style>
  :root {
    --green: #8cc04a;
    --green-dark: #6fa532;
    --green-deep: #5a8f26;
    --white: #ffffff;
    --paper-grey: #eef0ee;
    --stage: #e9ebea;
    --ink-soft: #6fa532;
    --photo-a: #c9b39a;
    --photo-b: #8a7660;
    --script: "Great Vibes", cursive;
    --sans: "Open Sans", sans-serif;
  }
  * { box-sizing: border-box; margin: 0; padding: 0; }
  html, body { width: 1200px; height: 800px; overflow: hidden; }
  body { background: var(--stage); font-family: var(--sans); position: relative; }

  .sheet {
    position: absolute; top: 193px; width: 585px; height: 414px;
    background: var(--green); overflow: hidden;
    box-shadow: 0 8px 24px rgba(0,0,0,.18);
  }
  .sheet--outside { left: 10px; }
  .sheet--inside { left: 605px; }
  .sheet__shapes { position: absolute; inset: 0; width: 100%; height: 100%; }
  .panel { position: absolute; top: 0; width: 195px; height: 414px; padding: 0 14px; }
  .panel--1 { left: 0; } .panel--2 { left: 195px; } .panel--3 { left: 390px; }
  .fold { position: absolute; top: 0; width: 1px; height: 100%; background: rgba(0,0,0,.07); }

  .script { font-family: var(--script); font-weight: 400; }
  .text-white { color: var(--white); }
  .text-green { color: var(--green-dark); }
  .abs { position: absolute; left: 14px; right: 14px; }
  .center { text-align: center; }
  .nowrap { white-space: nowrap; }
  .small { font-size: 6.8px; line-height: 1.35; }
  .heading { font-size: 9.5px; font-weight: 700; letter-spacing: .3px; }
  .headline-script { font-size: 27px; line-height: 1; }
  .tagline { font-size: 8px; font-weight: 600; line-height: 1.2; }
  .bullets { list-style: none; font-size: 6.8px; line-height: 1.45; font-weight: 600; }
  .bullets li::before { content: ""; display: inline-block; width: 4px; height: 4px; border-radius: 50%; background: currentColor; margin-right: 5px; vertical-align: 1px; }

  .photo {
    position: absolute; border-radius: 50%; border: 4px solid var(--white);
    box-shadow: 0 2px 6px rgba(0,0,0,.25);
    background: radial-gradient(circle at 40% 40%, var(--photo-a), var(--photo-b));
  }
  .photo--dogs {
    border-radius: 0; border: 0; box-shadow: none;
    background: linear-gradient(180deg, #f4f4f4 0%, #d9d4cc 60%, #b9a48a 100%);
  }
  .brand { display: flex; align-items: center; justify-content: center; gap: 6px; }
  .brand__dot { width: 10px; height: 10px; border-radius: 50%; background: var(--green-dark); }
  .brand__name { font-family: var(--sans); font-weight: 700; color: #333; white-space: nowrap; }
  .brand--large .brand__name { font-size: 18px; }
  .brand--small .brand__name { font-size: 8px; }
  .brand--small .brand__dot { width: 6px; height: 6px; }
  .logo-oval {
    position: absolute; top: 14px; width: 150px; height: 62px; border-radius: 50%;
    background: var(--white); box-shadow: 0 0 0 5px var(--green), 0 2px 6px rgba(0,0,0,.2);
    display: flex; align-items: center; justify-content: center;
  }
  .contact { display: grid; grid-template-columns: 30px 1fr; font-size: 6.8px; line-height: 1.35; font-weight: 600; }
  .url { font-size: 10px; font-weight: 700; letter-spacing: .3px; }
</style>
</head>
<body>

<section class="sheet sheet--outside" aria-label="Folder Außenseite">
  <svg class="sheet__shapes" viewBox="0 0 585 414" preserveAspectRatio="none" aria-hidden="true">
    <defs>
      <linearGradient id="paperA" x1="0" y1="0" x2="0" y2="1">
        <stop offset="0" stop-color="#ffffff"/><stop offset="1" stop-color="#eef0ee"/>
      </linearGradient>
    </defs>
    <path d="M195 0 H585 V292 C480 300 330 300 195 335 Z" fill="url(#paperA)"/>
    <path d="M0 352 C160 320 380 318 585 300" stroke="#ffffff" stroke-width="7" fill="none"/>
    <path d="M0 364 C170 334 390 330 585 314" stroke="#ffffff" stroke-width="1.5" fill="none" opacity=".7"/>
  </svg>

  <div class="panel panel--1">
    <p class="abs center small text-white" style="top:22px;font-weight:600;">Vereinbaren Sie einen Termin zur<br>Hundepflege von<br>Montag bis Samstag unter<br>Tel: (0201) 5 55 01 23 oder unter<br>info@pfote-mirella.de</p>
    <div class="photo" role="img" aria-label="Foto: frisch frisierter kleiner Terrier beim Föhnen" style="left:34px;top:90px;width:128px;height:78px;"></div>
    <p class="abs script text-white" style="top:180px;font-size:17px;">Wir bieten:</p>
    <ul class="abs bullets text-white" style="top:204px;">
      <li>Scheren- und Maschinenschnitt</li>
      <li>Effilieren + Entfilzen</li>
      <li>Auskämmen der Unterwolle</li>
      <li>Pfoten- &amp; Ballenpflege</li>
      <li>Kämmen, Baden &amp; Fönen</li>
    </ul>
    <ul class="abs bullets text-white" style="top:280px;">
      <li>liebevolle Einzelbetreuung</li>
      <li>flexible Öffnungszeiten</li>
      <li>chemiefreie Pflegeprodukte</li>
      <li>höchste Qualität</li>
    </ul>
    <p class="abs center script text-white" style="top:370px;font-size:13px;line-height:1.05;">Viele Gründe, bei uns vorbei zu schauen!<br>Wir freuen uns auf Ihren Besuch!</p>
  </div>

  <div class="panel panel--2">
    <p class="abs center script text-green headline-script" style="top:14px;">Hundesalon</p>
    <p class="abs center tagline text-green" style="top:44px;">... weil Fellpflege<br>Vertrauen braucht!</p>
    <p class="abs script text-green" style="top:74px;font-size:13px;">Liebe Kunden,</p>
    <p class="abs small text-green" style="top:92px;">der Hund ist unser treuester Begleiter – er hat es verdient, optimal versorgt zu werden. Gesunde Ernährung und gute Pflege können eine Menge dazu beitragen. Pfote Mirella bietet beides an: einen Hundeshop mit hochwertigen Artikeln und einen Hundesalon mit liebevoller Einzelbetreuung.</p>
    <p class="abs script text-green" style="top:166px;left:110px;font-size:14px;line-height:1;">Ihre Mirella<br>Kaufhold</p>
    <div class="photo" role="img" aria-label="Foto: Inhaberin mit ihrem hellen Hund" style="left:18px;top:204px;width:110px;height:82px;"></div>
    <div class="brand brand--small" style="position:absolute;left:122px;top:262px;"><span class="brand__dot"></span><span class="brand__name">Pfote Mirella</span></div>
    <div class="abs contact text-white" style="top:350px;">
      <span style="grid-column:1/3;">Mirella Kaufhold</span>
      <span style="grid-column:1/3;">Birkenweg 12, D-45133 Essen</span>
      <span>Tel:</span><span>(0201) 5 55 01 23</span>
      <span>Mobil:</span><span>(0170) 5 55 04 87</span>
      <span>eMail:</span><span>info@pfote-mirella.de</span>
      <span>Web:</span><span>www.pfote-mirella.de</span>
    </div>
  </div>

  <div class="panel panel--3" style="padding:0;">
    <div class="photo photo--dogs" role="img" aria-label="Foto: Schäferhund, Golden Retriever und Dalmatiner vor hellem Hintergrund" style="left:0;top:86px;width:195px;height:210px;"></div>
    <div class="logo-oval" style="left:22px;">
      <div class="brand brand--large"><span class="brand__dot"></span><span class="brand__name">Pfote Mirella</span></div>
    </div>
    <p class="center nowrap script text-white" style="position:absolute;left:0;right:0;top:352px;font-size:24px;line-height:1;">Hundesalon + Shop</p>
  </div>

  <span class="fold" style="left:195px;"></span><span class="fold" style="left:390px;"></span>
</section>

<section class="sheet sheet--inside" aria-label="Folder Innenseite">
  <svg class="sheet__shapes" viewBox="0 0 585 414" preserveAspectRatio="none" aria-hidden="true">
    <defs>
      <linearGradient id="paperB" x1="0" y1="0" x2="0" y2="1">
        <stop offset="0" stop-color="#ffffff"/><stop offset="1" stop-color="#eef0ee"/>
      </linearGradient>
    </defs>
    <path d="M195 0 H390 V318 C320 322 260 330 195 340 Z" fill="url(#paperB)"/>
    <path d="M0 345 C170 318 380 312 585 296" stroke="#ffffff" stroke-width="7" fill="none"/>
    <path d="M0 357 C170 330 390 326 585 310" stroke="#ffffff" stroke-width="1.5" fill="none" opacity=".7"/>
  </svg>

  <div class="panel panel--1">
    <p class="abs heading text-white" style="top:20px;">Halsbänder und Leinen</p>
    <p class="abs script text-white" style="top:36px;font-size:12px;">handgefertigt nach Ihren Wünschen</p>
    <ul class="abs bullets text-white" style="top:58px;">
      <li>extrem reißfest</li>
      <li>sehr leicht, daher hoher Tragekomfort</li>
      <li>Farbe und Muster individuell kombinierbar</li>
      <li>ein-, zwei- oder dreifarbig</li>
      <li>in 2cm, 3cm und 4cm Breite erhältlich</li>
      <li>wetterbeständig</li>
      <li>waschbar bei 30° C</li>
      <li>verschiedene Verschlüsse möglich</li>
    </ul>
    <div class="photo" role="img" aria-label="Foto: geflochtenes Halsband mit Muster" style="left:12px;top:186px;width:92px;height:72px;background:radial-gradient(circle,#b8453a,#3d2a22);"></div>
    <div class="photo" role="img" aria-label="Foto: bunte Halsbänder in Pink und Gelb" style="left:84px;top:230px;width:96px;height:72px;background:radial-gradient(circle,#e35aa0,#6b5a3a);"></div>
    <p class="abs small text-white" style="top:364px;font-weight:600;">In unserem Hundekiosk können Sie alles auch in kleinsten Mengen bestellen!</p>
    <p class="abs small text-white" style="top:388px;font-weight:600;">Und natürlich erhalten Sie bei uns eine kostenlose Beratung!</p>
  </div>

  <div class="panel panel--2">
    <p class="abs center script text-green headline-script" style="top:18px;">Hundeshop</p>
    <p class="abs center tagline text-green" style="top:48px;">... weil das Beste gerade gut<br>genug ist!</p>
    <p class="abs center script text-green" style="top:74px;font-size:14px;line-height:1.05;">Gesunde Kauartikel sowie Belohnungshappen und Hamburger aus reinem Fleisch</p>
    <div class="photo" role="img" aria-label="Foto: Kauknochen und getrocknete Kauartikel" style="left:28px;top:132px;width:140px;height:84px;background:radial-gradient(circle,#e0cdb0,#7d6a55);"></div>
    <ul class="abs bullets text-green" style="top:232px;">
      <li>ohne Konservierungsstoffe</li>
      <li>ohne Zucker</li>
      <li>ohne chemische Zusätze</li>
      <li>ohne Geschmacksverstärker</li>
      <li>gesund und fettarm</li>
      <li>selber mischen</li>
    </ul>
    <p class="center nowrap url text-white" style="position:absolute;left:0;right:0;top:370px;font-size:8.4px;">www.hundeshop-pfote-mirella.de</p>
  </div>

  <div class="panel panel--3">
    <p class="abs center heading text-white" style="top:20px;">Nahrungsergänzung*</p>
    <p class="abs center script text-white" style="top:36px;font-size:12px;">so einfach ist barfen</p>
    <div class="abs center small text-white" style="top:58px;font-weight:600;">
      <p>Pures Fleisch</p><p style="font-weight:400;">vom Rind, Lamm, Geflügel, Wild, ...</p><p>+</p>
      <p>Hochwertige Öle</p><p style="font-weight:400;">reich an Vitaminen und Omega-3-Fettsäuren</p><p>+</p>
      <p>Obst &amp; Gemüse</p><p style="font-weight:400;">tiefgefroren sowie Flockenmischungen</p><p>+</p>
      <p>Nahrungsergänzung</p><p style="font-weight:400;">bei Bedarf oder kurweise</p>
    </div>
    <p class="abs center script text-white" style="top:178px;font-size:14px;">Fertig ist die gesunde Mahlzeit!</p>
    <div class="photo" role="img" aria-label="Foto: Nahaufnahme eines kleinen Terriers" style="left:34px;top:204px;width:128px;height:80px;background:radial-gradient(circle,#b59e85,#5a4a3c);"></div>
    <p class="abs small text-white" style="top:362px;font-weight:600;">* BARF: Biologisch artgerechte Rohfütterung<br>Füttern von rohem Fleisch</p>
  </div>

  <span class="fold" style="left:195px;"></span><span class="fold" style="left:390px;"></span>
</section>

</body>
</html>
```